Brochure 11 x 25.5 Trifold

Brightlane Staffworks, Inc. is a payroll, benefits, and HR administration company. We are in need of a brochure to showcase all of our services. Attached is a one-page information sheet that contains the information we want in the brochure as well as several images. The brochure is a 11 x 25.5 tri-fold (a sample is attached). Please use the colors in the attached logo and design to complement our website brightlanestaff.example.
Target Market(s)
Company executives
Industry/Entity Type
Human Resource Management
Font styles to use
Other font styles liked:
- Avenir LT
Colors
Designer to choose colors to be used in the design.
Look and feel
Each slider illustrates characteristics of the customer's brand and the style your logo design should communicate.

```html
<!DOCTYPE html>
<html lang="en">
<head>
<meta charset="utf-8">
<title>Brightlane Staffworks – Trifold Brochure</title>
<link href="https://fonts.googleapis.com/css2?family=Nunito+Sans:wght@300;400;600;700;800&display=swap" rel="stylesheet">
<style>
:root{
  --navy:#0c3a5f;
  --navy-deep:#082c4a;
  --green:#8cb43f;
  --green-soft:#9cc04e;
  --paper:#eef0f2;
  --paper-2:#e3e6e9;
  --ink:#3d4650;
  --muted:#6d7680;
  --white:#ffffff;
  --stage:#d6d8db;
  --c-hiring:#e6a13a;
  --c-onboard:#d9b23a;
  --c-payroll:#4aa6c9;
  --c-benefits:#2b8fa3;
  --c-manage:#1f4f80;
  --c-separation:#d6552f;
}
*{margin:0;padding:0;box-sizing:border-box}
html,body{width:1200px;height:1124px;overflow:hidden}
body{background:var(--stage);font-family:"Nunito Sans",Arial,sans-serif;color:var(--ink);position:relative}
.spread{position:absolute;left:120px;width:960px;height:414px;background:var(--paper);overflow:hidden;box-shadow:0 6px 18px rgba(0,0,0,.25)}
.spread--outside{top:111px}
.spread--inside{top:613px}
.abs{position:absolute}
.photo{position:absolute;background:linear-gradient(135deg,#b9c0c6,#7d8893);}

/* outside – panel 1 */
.intro-band{left:0;top:0;width:350px;height:140px;background:var(--navy);border-radius:0 0 40px 0}
.intro-title{left:35px;top:30px;border-left:1.5px solid var(--green);padding-left:8px;line-height:1.05}
.intro-title .light{display:block;color:var(--green);font-weight:300;font-size:19px}
.intro-title .bold{display:block;color:var(--white);font-weight:800;font-size:19px}
.intro-copy{left:35px;top:82px;width:250px;color:var(--white);font-size:5.6px;line-height:1.35;text-align:justify}
.stage-label{position:absolute;width:72px;font-size:4.8px;line-height:1.4;color:var(--muted)}
.stage-label b{display:block;font-size:6.4px;font-weight:600;letter-spacing:.2px;margin-bottom:1px}
.lc-center{left:118px;top:260px;width:56px;text-align:center;font-size:8px;line-height:1;color:var(--navy)}
.lc-center b{font-weight:800}

/* outside – panel 2 */
.contact{left:362px;top:200px;color:var(--white)}
.contact h2{font-size:17px;font-weight:600;padding-bottom:3px;border-bottom:1.5px solid var(--white);display:inline-block;width:112px}
.contact-row{position:absolute;left:0;display:flex;gap:5px;font-size:6.6px;font-weight:600;line-height:1.4;white-space:nowrap}
.contact-row i{width:6px;height:6px;border:1px solid rgba(255,255,255,.8);border-radius:50%;margin-top:1.5px;flex:none}
.social{left:567px;top:376px;display:flex;gap:3px}
.social span{width:9px;height:9px;border-radius:50%;background:#9aa3ac}

/* outside – panel 3 */
.brand{display:flex;align-items:center;gap:6px;color:var(--navy);font-weight:600;line-height:1}
.brand i{background:var(--green);flex:none}
.cover-brand{left:688px;top:36px;font-size:13px}
.cover-brand i{width:16px;height:16px}
.cover-headline{left:686px;top:278px;border-left:1.5px solid var(--green);padding-left:6px;color:var(--white);line-height:1.05}
.cover-headline .light{display:block;font-size:18px;font-weight:400}
.cover-headline .bold{display:block;font-size:20px;font-weight:800}
.cover-headline .accent{display:block;font-size:20px;font-weight:800;color:var(--green);margin-left:-6px;margin-top:2px}
.cover-url{left:685px;top:377px;font-size:8.6px;letter-spacing:1.4px;color:var(--navy-deep);font-weight:600}
.cover-url span{color:var(--green)}

/* inside – panel 1 */
.apart-title{left:35px;top:186px;font-size:19px;color:var(--white);font-weight:400}
.apart-title b{color:var(--green);font-weight:700}
.apart-rule{left:35px;top:215px;width:248px;height:1px;background:rgba(255,255,255,.6)}
.feature{position:absolute;display:flex;gap:8px;width:118px}
.feature .dot{width:30px;height:30px;border-radius:50%;background:var(--green);flex:none;display:flex;align-items:center;justify-content:center}
.feature .dot i{width:15px;height:15px;border:1.5px solid var(--white);border-radius:3px}
.feature p{font-size:4.8px;line-height:1.4;color:var(--white);margin-top:2px}
.feature em{font-style:normal;color:var(--green);font-weight:700}
.feature--right{left:163px;width:122px}

/* inside – services */
.services-title{left:354px;top:24px;font-size:19px;font-weight:300;color:var(--green)}
.services-title b{color:var(--navy);font-weight:800}
.services-rule{left:354px;top:51px;width:250px;height:1px;background:var(--navy)}
.card{position:absolute;width:109px;background:var(--white);border:1px solid var(--navy);border-radius:0 0 8px 8px;box-shadow:0 2px 4px rgba(0,0,0,.15)}
.card h3{background:var(--navy);color:var(--green);font-size:9.5px;font-weight:700;line-height:1.05;padding:14px 8px 4px 10px;border-radius:6px 6px 0 0;margin:-1px -1px 0}
.card ul{list-style:none;padding:5px 6px 6px 12px}
.card li{font-size:4.5px;line-height:1.45;color:#222;position:relative}
.card li::before{content:"";position:absolute;left:-5px;top:1.5px;width:3px;height:3px;border:.6px solid var(--green);border-radius:50%}
.card .badge{position:absolute;right:8px;top:-12px;width:22px;height:22px;border-radius:50%;background:var(--green);border:1.5px solid var(--white);box-shadow:0 1px 2px rgba(0,0,0,.2);display:flex;align-items:center;justify-content:center;z-index:1}
.card .badge i{width:10px;height:10px;border:1.2px solid var(--white);border-radius:50%}

.back-brand{left:809px;top:160px;font-size:9px}
.back-brand i{width:11px;height:11px}
.back-slogan{left:809px;top:196px;border-left:1.5px solid var(--green);padding-left:6px;line-height:1.1;font-size:12px}
.back-slogan .light{display:block;color:var(--green);font-weight:400}
.back-slogan .bold{display:block;color:var(--navy);font-weight:800}
.bottom-stripe{left:0;bottom:0;width:960px;height:3px;background:var(--green)}
</style>
</head>
<body>

<section class="spread spread--outside" aria-label="Brochure outside spread">
  <!-- panel 1 -->
  <div class="abs" style="left:0;top:0;width:320px;height:414px;background:linear-gradient(120deg,#f6f7f8,#e7e9eb)"></div>
  <div class="abs intro-band"></div>
  <h1 class="abs intro-title"><span class="light">From hire to retire,</span><span class="bold">we’ve got you covered</span></h1>
  <p class="abs intro-copy">Brightlane Staffworks has been delivering quality HR and Payroll services for over 25 years. Our dedicated team of professionals is focused on being the best service provider in the industry. Our goal is to relieve business executives of the challenges of managing a dynamic and growing workforce in today’s regulatory environment and give them the freedom to focus on what drives their business.</p>

  <svg class="abs" style="left:0;top:0" width="320" height="414" viewBox="0 0 320 414" aria-hidden="true">
    <g fill="none" stroke-width="1.2" stroke-linecap="round">
      <path d="M145 221 A49 49 0 0 1 189 248" stroke="var(--c-hiring)"/>
      <path d="M193 256 A49 49 0 0 1 185 298" stroke="var(--c-onboard)"/>
      <path d="M180 304 A49 49 0 0 1 145 319" stroke="var(--c-payroll)"/>
      <path d="M137 318 A49 49 0 0 1 100 290" stroke="var(--c-benefits)"/>
      <path d="M97 281 A49 49 0 0 1 108 238" stroke="var(--c-manage)"/>
      <path d="M114 232 A49 49 0 0 1 146 221" stroke="var(--c-separation)"/>
      <path d="M145 213 L145 200 L178 200" stroke="var(--c-hiring)" stroke-width=".8"/>
      <path d="M193 245 L205 236" stroke="var(--c-onboard)" stroke-width=".8"/>
      <path d="M194 290 L207 297" stroke="var(--c-payroll)" stroke-width=".8"/>
      <path d="M145 326 L145 338" stroke="var(--c-benefits)" stroke-width=".8"/>
      <path d="M96 298 L84 305" stroke="var(--c-manage)" stroke-width=".8"/>
      <path d="M104 236 L92 232" stroke="var(--c-separation)" stroke-width=".8"/>
    </g>
  </svg>
  <div class="abs lc-center">EMPLOYEE<br><b>LIFECYCLE</b></div>
  <div class="stage-label" style="left:127px;top:158px"><b style="color:var(--c-hiring)">HIRING</b>Integrated cloud-based ATS, Auto post to job boards, applicant management and screening</div>
  <div class="stage-label" style="left:42px;top:208px;width:48px"><b style="color:var(--c-separation)">SEPARATION</b>COBRA, Retirement plan assistance, DOL Notining</div>
  <div class="stage-label" style="left:210px;top:215px;width:58px"><b style="color:var(--c-onboard)">ONBOARDING</b>Auto generate notice to new-hire, standard and customized forms and acknowledgements</div>
  <div class="stage-label" style="left:213px;top:288px;width:46px"><b style="color:var(--c-payroll)">PAYROLL</b>HRIS, Direct deposits, New Hire Reporting, Employee Portal, Year End Reporting</div>
  <div class="stage-label" style="left:44px;top:300px;width:62px"><b style="color:var(--c-manage)">EMPLOYEE<br>MANAGEMENT</b>Culture development, discipline, leave management, Workers’ Compensation claims, employee verifications, handbook</div>
  <div class="stage-label" style="left:131px;top:337px;width:66px"><b style="color:var(--c-benefits)">BENEFITS</b>Online enrollment, application, benefit reconciliations, eligibility tracking notifications, retirement plan</div>

  <!-- panel 2 -->
  <div class="abs" style="left:320px;top:0;width:320px;height:414px;background:linear-gradient(180deg,#eceef0,#e2e5e8)"></div>
  <div class="photo" role="img" aria-label="Photo: team meeting around a desk with a manager reviewing documents" style="left:320px;top:0;width:320px;height:190px;background:linear-gradient(90deg,#dfe2e5 0%,#b8bec4 45%,#6b5a4c 60%,#3e3833 80%,#c9b59a 100%)"></div>

  <!-- panel 3 -->
  <div class="abs" style="left:640px;top:0;width:320px;height:414px;background:linear-gradient(120deg,#f4f5f6,#e6e8ea)"></div>
  <svg class="abs" style="left:0;top:0" width="960" height="414" viewBox="0 0 960 414" aria-hidden="true">
    <path d="M928 0 H960 V52 Q935 42 928 20 Z" fill="var(--green)"/>
    <path d="M960 340 V414 H925 Q938 390 944 362 Q950 344 960 340 Z" fill="var(--green)"/>
    <path d="M600 149 H950 Q962 149 960 164 L925 350 Q922 363 908 363 H548 Q530 363 534 346 L566 166 Q570 149 600 149 Z" fill="var(--navy)"/>
    <path d="M560 200 H935" stroke="var(--green)" stroke-width=".6" fill="none" opacity=".6"/>
    <path d="M352 185 H566 Q583 185 579 202 L542 375 Q538 390 520 390 H272 Q252 390 257 372 L308 200 Q313 185 352 185 Z" fill="var(--green)" opacity=".92"/>
    <path d="M360 196 H560 Q570 196 567 207 L534 366 Q532 376 521 376 H285 Q273 376 276 366 L323 206 Q326 196 340 196 Z" fill="none" stroke="rgba(255,255,255,.55)" stroke-width=".7"/>
    <path d="M890 365 Q925 362 930 330 L955 210" fill="none" stroke="var(--green)" stroke-width=".6" opacity=".6"/>
  </svg>
  <div class="photo" role="img" aria-label="Photo: cheerful woman at a laptop with raised hands in a bright office" style="left:640px;top:81px;width:311px;height:182px;border-radius:0 44px 0 0;background:linear-gradient(110deg,#e98a1e 0%,#f0b93a 22%,#8c8f95 45%,#4e5560 70%,#8b6b4e 100%)"></div>

  <div class="abs contact"><h2>Get In Touch</h2></div>
  <div class="abs contact" style="top:0">
    <div class="contact-row" style="top:253px"><i></i><span>412 Harrow Court<br>Lakeview, ST 00412</span></div>
    <div class="contact-row" style="top:290px"><i></i><span>555-014-3000</span></div>
    <div class="contact-row" style="top:301px"><i></i><span>1-800-555-0172</span></div>
    <div class="contact-row" style="top:313px"><i></i><span>555-014-1488</span></div>
    <div class="contact-row" style="top:338px"><i></i><span>info@brightlanestaff.example</span></div>
    <div class="contact-row" style="top:350px"><i></i><span>www.brightlanestaff.example</span></div>
  </div>
  <div class="abs social" aria-hidden="true"><span></span><span></span><span></span><span></span></div>

  <div class="abs brand cover-brand"><i></i><span>BRIGHTLANE STAFFWORKS</span></div>
  <h2 class="abs cover-headline"><span class="light">Your single-source</span><span class="bold">solution for</span><span class="accent">ENTIRE EMPLOYEE</span></h2>
  <div class="abs cover-url">www.<span>brightlanestaff</span>.example</div>
</section>

<section class="spread spread--inside" aria-label="Brochure inside spread">
  <!-- panel 1 -->
  <div class="abs" style="left:0;top:0;width:320px;height:414px;background:linear-gradient(160deg,#f3f4f5,#e4e7ea)"></div>
  <svg class="abs" style="left:0;top:0" width="320" height="414" viewBox="0 0 320 414" aria-hidden="true">
    <path d="M0 159 L320 106 V414 H0 Z" fill="var(--navy)"/>
  </svg>
  <div class="photo" role="img" aria-label="Image: payroll portal dashboard shown on a laptop and a phone" style="left:45px;top:33px;width:277px;height:140px;background:linear-gradient(180deg,#f8f9fa 0%,#e3e7ea 70%,#9aa4ad 100%);border-radius:6px"></div>

  <h2 class="abs apart-title">What <b>Sets Us Apart?</b></h2>
  <div class="abs apart-rule"></div>
  <div class="feature" style="left:35px;top:238px"><span class="dot"><i></i></span><p>Our <em>dedicated team of experts</em> is always just a call or email away! You get direct phone numbers to the professionals you need!</p></div>
  <div class="feature feature--right" style="top:238px"><span class="dot"><i></i></span><p>Our <em>advanced software</em> is used to process payroll for over 88,000 companies and 2.2 million employees nation-wide. It makes even the most complex payrolls easy.</p></div>
  <div class="feature" style="left:35px;top:292px"><span class="dot"><i></i></span><p><em>Access your employee information how you need it when you need it</em> with our quick-access reports and intuitive report writer. We even provide custom reports!</p></div>
  <div class="feature feature--right" style="top:292px"><span class="dot"><i></i></span><p>We are equipped with <em>education, experience, certifications, and motivation.</em> Our staff executes at the highest level in payroll and HR every day.</p></div>
  <div class="feature" style="left:35px;top:348px"><span class="dot"><i></i></span><p>Employee information is automatically integrated across all modules, <em>eliminating duplicate data entry and significantly reducing errors.</em></p></div>
  <div class="feature feature--right" style="top:348px"><span class="dot"><i></i></span><p>Our <em>client branded, cloud-based Employee and Manager portals</em> allow your employees to access their payroll information quicker and more securely than ever before!</p></div>

  <!-- panel 2 -->
  <div class="abs" style="left:320px;top:0;width:320px;height:414px;background:linear-gradient(180deg,#f1f2f3,#e6e8ea)"></div>
  <h2 class="abs services-title">Our <b>Services</b></h2>
  <div class="abs services-rule"></div>

  <div class="card" style="left:354px;top:71px"><span class="badge"><i></i></span><h3>Payroll</h3><ul><li>Fast, efficient, accurate</li><li>Paper checks or direct deposit</li><li>Easy time file uploads or integrated time clock options</li><li>New hire reporting</li><li>Custom G/L file</li><li>Comprehensive reporting options</li><li>Certified payroll option</li></ul></div>
  <div class="card" style="left:495px;top:71px"><span class="badge"><i></i></span><h3>Human Resource<br>Administration</h3><ul><li>Wage and hour compliance</li><li>Employee handbooks</li><li>Performance management</li><li>Employee discipline and termination consulting</li><li>Workers’ comp claims administration</li><li>Unemployment administration</li><li>Manager training</li></ul></div>
  <div class="card" style="left:354px;top:186px"><span class="badge"><i></i></span><h3>Benefits<br>Management</h3><ul><li>Customized benefits packet</li><li>Track new hire eligibility</li><li>Open enrollment assistance</li><li>Electronic enrollment</li><li>Track and submit enrollments</li><li>Provide 401k census report</li><li>Remit retirement plan reports &amp; funds</li><li>ACA compliance</li></ul></div>
  <div class="card" style="left:495px;top:190px"><span class="badge"><i></i></span><h3>Time and<br>Attendance</h3><ul><li>Integrated with payroll (no double entry)</li><li>Mobile and geofencing options</li><li>Overtime notices</li><li>Online time-off requests</li><li>Swipe and proximity card clocks</li><li>Biometric clocks</li><li>PTO tracking</li></ul></div>
  <div class="card" style="left:354px;top:306px"><span class="badge"><i></i></span><h3>Employee<br>Onboarding</h3><ul><li>Simple, accurate, paperless</li><li>Custom forms and acknowledgements</li><li>Standard forms (W-4, I-9, State withholding, etc)</li><li>Paperless, electronic signatures</li><li>Employee handbook and policy acknowledgements</li><li>Custom welcome videos</li></ul></div>
  <div class="card" style="left:495px;top:306px"><span class="badge"><i></i></span><h3>Talent<br>Acquisition</h3><ul><li>Custom careers page</li><li>Standard or custom job applications</li><li>Easy conversion of applicant data to employee data</li><li>Review, rate, and contact applicants</li><li>Mobile-friendly access</li><li>Easy posting to top job boards</li><li>Candidate screening</li></ul></div>

  <!-- panel 3 -->
  <div class="abs" style="left:640px;top:0;width:320px;height:414px;background:linear-gradient(160deg,#f4f5f6,#e5e7e9)"></div>
  <div class="card" style="left:674px;top:41px"><span class="badge"><i></i></span><h3>COBRA<br>Administration</h3><ul><li>Initial notices</li><li>Open enrollment notices</li><li>Easy 24/7 online reporting</li><li>Qualified beneficiary election notices</li><li>Premium collection</li><li>Access to professional advice</li></ul></div>
  <div class="card" style="left:815px;top:41px"><span class="badge"><i></i></span><h3>Cafeteria<br>FSA/HRA<br>Administration</h3><ul><li>Plan documents/materials</li><li>Debit cards</li><li>Easy 24/7 online reporting</li><li>Claims processing</li><li>Plan testing</li></ul></div>
  <div class="card" style="left:674px;top:153px"><span class="badge"><i></i></span><h3>Compliance</h3><ul><li>Certified experts ensure compliance with all labor laws and regulations</li><li>OSHA Reporting</li><li>Affirmative Action (EEOC)</li><li>Affordable Care Act (ACA)</li><li>Family Medical Leave Act (FMLA)</li><li>Workers’ Comp audits</li></ul></div>

  <div class="abs brand back-brand"><i></i><span>BRIGHTLANE STAFFWORKS</span></div>
  <h2 class="abs back-slogan"><span class="light">SAVE TIME AND<br>STAY FOCUSED ON</span><span class="bold">RUNNING<br>YOUR BUSINESS</span></h2>
  <div class="photo" role="img" aria-label="Photo: business professionals shaking hands across a meeting table" style="left:640px;top:268px;width:320px;height:146px;background:linear-gradient(90deg,#e9ebec 0%,#2c2f36 25%,#c9ced3 50%,#e8eaeb 70%,#3a3230 90%,#d4d8db 100%)"></div>
  <div class="abs bottom-stripe"></div>
</section>

</body>
</html>
```